Website Design for Law Firm

We need a fresh new website design for our client 'Vendrick Legal' who specialises as a Criminal, Traffic & Civil Lawyer in Perth, Western Australia. We are looking for a very clean, professional and elegant look for the website, a presence of power and class needed as he deals with high end clients. Black, Silver and hints of gold need to run through the design without making the site look too dark. We are after a very modern, spacious web look, use of large readable text with links to social media (such as Chatterloom, Zumbly+, Quibbr, WorkMesh) to stand out and his contact details to be made very predominate.

Reason: Public holidays here in Australia, need more business hours to discuss designs with client.

Reason: Client needs more time to look through designs.

Reason: Client is going over last of designs. Design will be picked early next week!

Industry/Entity Type

Law Firm

```html
<!DOCTYPE html>
<html lang="en">
<head>
<meta charset="utf-8">
<title>Vendrick Legal</title>
<link rel="stylesheet" href="https://fonts.googleapis.com/css2?family=Open+Sans:wght@300;400;600&family=Arimo:wght@400&display=swap">
<style>
:root{
  --ink:#1d1d1d;
  --text:#555;
  --muted:#777;
  --silver:#dcdcdc;
  --line:#c9c9c9;
  --gold:#e8b923;
  --white:#fff;
  --footer:#565656;
  --button:#4a4a4a;
}
*{margin:0;padding:0;box-sizing:border-box}
html,body{width:1200px;height:3111px;overflow:hidden;background:var(--white)}
body{position:relative;font-family:"Open Sans",sans-serif;color:var(--text)}
.abs{position:absolute}

/* header */
.site-header{left:0;top:0;width:1200px;height:147px}
.brand{left:86px;top:46px;display:flex;align-items:center;gap:12px}
.brand-mark{width:26px;height:26px;background:var(--ink)}
.brand-name{font-size:30px;font-weight:600;letter-spacing:1px;color:var(--ink);line-height:1}
.main-nav{left:503px;top:70px;display:flex;align-items:center;height:36px}
.main-nav a{font-size:16px;color:var(--ink);text-decoration:none;padding:0 24px;line-height:36px;border-left:1px solid var(--line)}
.main-nav a:nth-child(2){border-left:none}
.main-nav a.is-active{background:var(--ink);color:var(--white);padding:0 22px;border:none}

/* hero */
.hero{left:0;top:147px;width:1200px;height:593px;
  background:linear-gradient(180deg,#233a2a 0%,#2f5335 30%,#3c6440 55%,#5a4a2c 78%,#2a241a 100%)}
.hero-shade{left:0;top:147px;width:1200px;height:593px;background:rgba(0,0,0,.25)}
.hero-rule{left:259px;width:682px;height:1px;background:rgba(255,255,255,.45)}
.hero-title{left:0;width:1200px;top:370px;text-align:center;color:var(--white);font-weight:300;font-size:70px;line-height:1}
.hero-sub{left:0;width:1200px;top:485px;text-align:center;color:var(--white);font-weight:300;font-size:38px;line-height:1}
.hero-arrow{top:395px}

/* services */
.services{left:0;top:740px;width:1200px;height:643px;background:var(--silver)}
.section-heading{font-weight:400;color:var(--ink);line-height:1}
.services-title{left:86px;top:820px;font-size:62px}
.services-intro{left:424px;top:818px;width:690px;font-size:13px;line-height:25px;color:var(--text)}
.services-rule{left:86px;top:947px;width:1028px;height:1px;background:#cfcfcf}
.service-card{top:1065px;width:310px;height:245px;background:var(--white);border-top:6px solid var(--gold);text-align:center;box-shadow:0 2px 3px rgba(0,0,0,.08)}
.service-icon{position:absolute;left:96px;top:-65px;width:118px;height:118px;border-radius:50%;background:var(--white);box-shadow:0 1px 4px rgba(0,0,0,.18);display:flex;align-items:center;justify-content:center}
.service-name{margin-top:83px;font-size:21px;color:#333;letter-spacing:.5px}
.service-text{margin:20px auto 0;width:258px;font-size:13.5px;line-height:25px;color:var(--muted)}

/* about */
.about-title{left:0;width:1200px;top:1455px;text-align:center;font-size:45px}
.about-photo{left:86px;top:1556px;width:453px;height:244px;
  background:linear-gradient(135deg,#2a3550 0%,#6b4a2e 40%,#4a2a18 60%,#c9b58f 85%,#e9dcc0 100%)}
.about-body{left:602px;top:1556px;width:512px}
.about-lead{font-size:21px;color:#333;margin-bottom:10px}
.about-body p{font-size:13.5px;line-height:25px;color:var(--text);margin-bottom:8px}

/* testimonials */
.testimonials{left:0;top:1888px;width:1200px;height:390px;
  background:linear-gradient(90deg,#1a2433 0%,#2b3a52 40%,#3a4a68 65%,#1c2638 100%)}
.testimonials-shade{left:0;top:1888px;width:1200px;height:390px;background:rgba(0,0,0,.35)}
.quote-mark{left:0;width:1200px;top:1948px;text-align:center;color:var(--white);font-size:74px;font-weight:600;line-height:1}
.testimonials-title{left:0;width:1200px;top:2030px;text-align:center;color:var(--white);font-size:34px;font-weight:400}
.testimonial-text{left:140px;top:2095px;width:920px;text-align:center;color:var(--white);font-size:15.5px;line-height:30px}
.testimonial-author{left:0;width:1200px;top:2203px;text-align:center;color:var(--white);font-size:17px}
.testimonial-author small{font-size:13px}
.slider-dots{left:0;width:1200px;top:2259px;display:flex;justify-content:center;gap:6px}
.slider-dots span{width:10px;height:10px;border-radius:50%;background:#ccc}
.slider-dots span.is-current{background:#777}

/* contact */
.contact-title{left:0;width:1200px;top:2404px;text-align:center;font-size:45px}
.form-label{left:138px;font-family:"Arimo",sans-serif;font-size:15px;color:#333}
.form-field{left:138px;width:446px;border:2px solid #dedede;background:var(--white);font-family:"Arimo",sans-serif;font-size:15px;color:#444;padding:14px 16px}
.send-button{left:474px;top:2883px;width:110px;height:47px;background:var(--button);color:var(--white);font-family:"Arimo",sans-serif;font-size:17px;display:flex;align-items:center;justify-content:center}
.map{left:683px;top:2513px;width:402px;height:164px;background:linear-gradient(135deg,#e9e4d6 0%,#d9dcc9 45%,#c8d6e0 100%);border:1px solid #ddd}
.contact-line{font-size:14px;color:#444;line-height:30px}
.social-links{left:690px;top:2835px;display:flex;gap:22px}
.social-item{display:flex;flex-direction:column;align-items:center;width:74px}
.social-dot{width:58px;height:58px;border-radius:50%;background:#5a6d8a}
.social-name{margin-top:6px;font-size:12px;color:#444;white-space:nowrap}

/* footer */
.site-footer{left:0;top:2989px;width:1200px;height:122px;background:var(--footer)}
.footer-links{left:88px;top:3027px;font-family:"Arimo",sans-serif;font-size:14px;color:var(--white)}
.footer-copy{left:88px;top:3062px;font-family:"Arimo",sans-serif;font-size:14px;color:var(--white)}
</style>
</head>
<body>

<header class="site-header abs">
  <div class="brand abs"><span class="brand-mark"></span><span class="brand-name">VENDRICK LEGAL</span></div>
  <nav class="main-nav abs">
    <a class="is-active" href="#">HOME</a>
    <a href="#">ABOUT US</a>
    <a href="#">SERVICES</a>
    <a href="#">TESTIMONIALS</a>
    <a href="#">CONTACT</a>
  </nav>
</header>

<section>
  <div class="hero abs" role="img" aria-label="Blurred shelf of green leather-bound law books"></div>
  <div class="hero-shade abs"></div>
  <div class="hero-rule abs" style="top:350px"></div>
  <h1 class="hero-title abs">POWERFUL</h1>
  <p class="hero-sub abs">PROTECTION OF OUR CLIENTS</p>
  <div class="hero-rule abs" style="top:562px"></div>
  <svg class="hero-arrow abs" style="left:52px" width="36" height="96" viewBox="0 0 36 96"><polyline points="34,2 2,48 34,94" fill="none" stroke="#fff" stroke-width="2"/></svg>
  <svg class="hero-arrow abs" style="left:1112px" width="36" height="96" viewBox="0 0 36 96"><polyline points="2,2 34,48 2,94" fill="none" stroke="#fff" stroke-width="2"/></svg>
</section>

<section>
  <div class="services abs"></div>
  <h2 class="section-heading services-title abs">SERVICES</h2>
  <p class="services-intro abs">Duis autem vel eum iriure dolor in hendrerit in vulputate velit esse molestie consequat, vel illum dolore eu feugiat nulla facilisis at vero eros et accumsan et iusto. Nam liber tempor cum soluta nobis eleifend option congue nihil imperdiet doming. Nam liber tempor cum soluta nobis eleifend option congue nihil imperdiet.</p>
  <div class="services-rule abs"></div>

  <article class="service-card abs" style="left:86px">
    <div class="service-icon">
      <svg width="52" height="48" viewBox="0 0 52 48" fill="#222"><polygon points="26,2 50,14 2,14"/><rect x="4" y="16" width="44" height="4"/><rect x="8" y="22" width="6" height="16"/><rect x="19" y="22" width="6" height="16"/><rect x="29" y="22" width="6" height="16"/><rect x="39" y="22" width="6" height="16"/><rect x="2" y="40" width="48" height="6"/></svg>
    </div>
    <h3 class="service-name">CRIMINAL LAW</h3>
    <p class="service-text">Claritas est etiam processus dynamicus, qui sequitur mutationem consuetudium lectorum. Mirum est notare</p>
  </article>

  <article class="service-card abs" style="left:447px">
    <div class="service-icon">
      <svg width="52" height="48" viewBox="0 0 52 48" fill="#222"><rect x="20" y="4" width="14" height="24" rx="2" transform="rotate(45 27 16)"/><rect x="10" y="26" width="5" height="22" rx="2" transform="rotate(45 12 37)"/><rect x="4" y="42" width="26" height="5"/></svg>
    </div>
    <h3 class="service-name">TRAFFIC LAW</h3>
    <p class="service-text">Claritas est etiam processus dynamicus, qui sequitur mutationem consuetudium lectorum. Mirum est notare</p>
  </article>

  <article class="service-card abs" style="left:805px">
    <div class="service-icon">
      <svg width="54" height="50" viewBox="0 0 54 50" fill="none" stroke="#222" stroke-width="3"><line x1="27" y1="4" x2="27" y2="44"/><line x1="8" y1="10" x2="46" y2="10"/><path d="M8 10 L2 26 H14 Z"/><path d="M46 10 L40 26 H52 Z"/><line x1="16" y1="46" x2="38" y2="46"/></svg>
    </div>
    <h3 class="service-name">CIVIL LAW</h3>
    <p class="service-text">Claritas est etiam processus dynamicus, qui sequitur mutationem consuetudium lectorum. Mirum est notare</p>
  </article>
</section>

<section>
  <h2 class="section-heading about-title abs">ABOUT US</h2>
  <div class="about-photo abs" role="img" aria-label="Wooden judge's gavel resting on an open book"></div>
  <div class="about-body abs">
    <h3 class="about-lead">Duis autem vel eum iriur!</h3>
    <p>Typi non habent claritatem insitam; est usus legentis in iis qui facit eorum claritatem. Investigationes demonstraverunt lectores legere me lius quod ii legunt saepius.</p>
    <p>Claritas est etiam processus dynamicus, qui sequitur mutationem consuetudium lectorum. Mirum est notare quam littera gothica, quam nunc putamus parum claram, anteposuerit litterarum formas humanitatis per seacula quarta decima et quinta decima. Eodem modo typi, qui nunc nobis videntur parum clari, fiant sollemnes in futurum.</p>
  </div>
</section>

<section>
  <div class="testimonials abs" role="img" aria-label="Close-up of a clock face in dark blue tones"></div>
  <div class="testimonials-shade abs"></div>
  <div class="quote-mark abs">&ldquo;</div>
  <h2 class="testimonials-title abs">TESTIMONIALS</h2>
  <p class="testimonial-text abs">Lorem ipsum dolor sit amet, consectetur adipisicing elit. Etmodi liberomus quos recusandae quibusdam autem fuga accusantium iste nam culpa expedita nisi inventore tenetur ipsa eligendi arcto. Eveniet Lorem ipsuor sit amet, cotetur. Lorem ipsum dolor sit amet, consectetur adipiscing elit. Integer ac vula tortor, vitae lacinia nisi. Mauris ac urna.</p>
  <p class="testimonial-author abs">- LIAM CARTER, <small>MANAGER AT NORVALE</small></p>
  <div class="slider-dots abs"><span></span><span class="is-current"></span><span class="is-current"></span><span class="is-current"></span></div>
</section>

<section>
  <h2 class="section-heading contact-title abs">CONTACT US</h2>

  <label class="form-label abs" style="top:2496px">Name</label>
  <div class="form-field abs" style="top:2522px;height:52px">Your Name</div>
  <label class="form-label abs" style="top:2604px">Email</label>
  <div class="form-field abs" style="top:2630px;height:52px">Email id</div>
  <label class="form-label abs" style="top:2719px">Message</label>
  <div class="form-field abs" style="top:2745px;height:111px">send your message</div>
  <div class="send-button abs">SEND</div>

  <div class="map abs" role="img" aria-label="Street map showing the office location"></div>

  <svg class="abs" style="left:682px;top:2743px" width="14" height="20" viewBox="0 0 14 20"><path d="M7 0a7 7 0 0 0-7 7c0 5 7 13 7 13s7-8 7-13a7 7 0 0 0-7-7z" fill="#444"/><circle cx="7" cy="7" r="2.5" fill="#fff"/></svg>
  <div class="contact-line abs" style="left:715px;top:2735px">240 Halvern Street<br>Perth WA 6000</div>

  <svg class="abs" style="left:916px;top:2745px" width="18" height="13" viewBox="0 0 18 13"><rect width="18" height="13" fill="#444"/><polyline points="0,0 9,7 18,0" fill="none" stroke="#fff" stroke-width="1.5"/></svg>
  <svg class="abs" style="left:917px;top:2773px" width="16" height="16" viewBox="0 0 16 16"><path d="M3 0l3 4-2 2c1 2 3 4 6 6l2-2 4 3-2 3C7 16 0 9 0 3z" fill="#444"/></svg>
  <div class="contact-line abs" style="left:952px;top:2735px">info@vendrickmail.com<br>84 555 0192</div>

  <div class="social-links abs">
    <div class="social-item"><span class="social-dot"></span><span class="social-name">Chatterloom</span></div>
    <div class="social-item"><span class="social-dot"></span><span class="social-name">Quibbr</span></div>
    <div class="social-item"><span class="social-dot"></span><span class="social-name">Zumbly+</span></div>
    <div class="social-item"><span class="social-dot"></span><span class="social-name">WorkMesh</span></div>
  </div>
</section>

<footer class="site-footer abs"></footer>
<p class="footer-links abs">Terms and Conditions | Privacy Promise | FAQ's | Contact Us</p>
<p class="footer-copy abs">Copyright &copy; 2013. All Rights Reserved.</p>

</body>
</html>
```